Home Security check flyer

I am a locksmith company. Wanting a flyer designed for postal delivery to houses.
The design is to have a home security check list similar to the one attached (Not exactly the same) targeting locks with some pictures of deadlocks, Deadbolts, Window Locks, Security door locks Etc..
The idea is to get people in there homes to make sure they are secure and if not to call us for a free quote.
Flyer is to catch customers eye so they don't just throw it our. E.G. IS YOUR HOME SECURE on the front
A4 Size to be folded to twice to envelope size.
My company information can be found at
www.brightkeyworks.com.au

Reason: Want to try a few changes on some of the eliminated ones.

Target Market(s)

residential homes (Security)

Industry/Entity Type

Locksmith

Requirements
Must have
• My logo and contact information
Based on information from www.brightkeyworks.com.au

```html
<!DOCTYPE html>
<html lang="en">
<head>
<meta charset="utf-8">
<title>Brightkey Works – Home Security Check Flyer</title>
<link href="https://fonts.googleapis.com/css2?family=Archivo+Black&family=Arimo:wght@400;700&display=swap" rel="stylesheet">
<style>
  :root {
    --stone: #cdc9c2;
    --stone-light: #d8d4ce;
    --charcoal: #3a3e41;
    --red: #c8191e;
    --white: #ffffff;
    --ink: #4a4d50;
    --brick: #8a4a3a;
  }
  * { box-sizing: border-box; margin: 0; padding: 0; }
  html, body { width: 1200px; height: 830px; overflow: hidden; background: var(--white); }
  body { position: relative; font-family: "Arimo", Arial, sans-serif; }

  .panel { position: absolute; top: 28px; width: 553px; height: 774px; overflow: hidden; }
  .panel--front { left: 24px; background: linear-gradient(180deg, var(--stone-light) 0%, var(--stone) 45%); }
  .panel--back { left: 624px; width: 552px; background: var(--stone); }

  .brand { font-family: "Arimo", Arial, sans-serif; font-weight: 700; color: var(--red); display: flex; align-items: center; gap: 6px; }
  .brand__dot { width: 12px; height: 12px; border-radius: 50%; background: var(--red); }

  /* front */
  .hero-photo {
    position: absolute; left: 0; top: 330px; width: 100%; height: 444px;
    background:
      linear-gradient(180deg, var(--stone) 0%, rgba(205,201,194,0) 25%),
      linear-gradient(90deg, #f2f0ec 0%, #e4e0da 22%, #b9a79c 48%, var(--brick) 70%, #6f3a2e 100%);
  }
  .front__brand { position: absolute; right: 22px; top: 16px; font-size: 22px; }
  .front__lead { position: absolute; left: 16px; top: 12px; font-family: "Archivo Black", "Arial Black", sans-serif; font-size: 44px; color: var(--charcoal); }
  .front__title { position: absolute; left: 40px; top: 48px; font-family: "Archivo Black", "Arial Black", sans-serif; font-size: 150px; line-height: 1; color: var(--white); letter-spacing: -2px; }
  .front__copy { position: absolute; left: 0; width: 100%; top: 200px; text-align: center; font-weight: 700; }
  .front__peace { font-size: 26px; color: var(--charcoal); }
  .front__secure { font-size: 33px; color: var(--white); line-height: 39px; margin-top: 3px; }
  .front__secure em { font-style: normal; color: var(--red); font-size: 36px; }
  .front__turn { font-size: 20px; color: var(--charcoal); line-height: 24px; margin-top: 14px; }
  .front__turn em { font-style: normal; color: var(--red); }

  /* back */
  .back__intro { position: absolute; left: 0; top: 16px; width: 100%; text-align: center; }
  .back__headline { font-size: 19px; font-weight: 700; color: var(--white); line-height: 23px; }
  .back__advice { font-size: 16px; color: var(--charcoal); line-height: 20px; margin-top: 6px; }
  .back__question { font-size: 18px; font-weight: 700; color: var(--white); line-height: 23px; margin-top: 4px; }
  .back__question em { font-style: normal; color: var(--red); }

  .checklist { position: absolute; left: 31px; top: 194px; width: 492px; height: 421px; background: var(--white); border: 3px solid var(--red); border-radius: 4px; }
  .checklist__head { position: absolute; left: 12px; top: 11px; width: 462px; height: 53px; background: var(--charcoal); color: var(--white); font-weight: 700; display: flex; justify-content: space-between; align-items: center; padding: 0 12px 0 10px; }
  .checklist__head-left { font-size: 17px; padding-top: 4px; }
  .checklist__head-right { font-size: 16px; text-align: right; line-height: 20px; }
  .checklist__body { position: absolute; left: 12px; top: 70px; width: 400px; }
  .group { margin-top: 11px; }
  .group:first-child { margin-top: 0; }
  .group__title { font-size: 12px; color: var(--red); line-height: 13px; }
  .item { display: grid; grid-template-columns: 125px 13px 20px 7px 15px 20px 25px 1fr; align-items: center; height: 12.3px; font-size: 10.5px; color: var(--ink); }
  .item__yn { font-size: 7px; font-weight: 700; color: var(--charcoal); }
  .item__box { width: 20px; height: 11px; border: 1px solid var(--charcoal); }
  .item__note { grid-column: 8; font-size: 6.2px; color: var(--ink); white-space: nowrap; }
  .checklist__cta { position: absolute; left: 0; width: 100%; bottom: 12px; text-align: center; font-size: 16px; color: var(--red); }

  .lock-photo { position: absolute; left: 418px; width: 56px; border-radius: 6px; background: linear-gradient(135deg, #e6e6e4, #9a9a98); }

  .contact-bar { position: absolute; left: 16px; top: 635px; width: 520px; height: 72px; background: var(--red); color: var(--white); font-weight: 700; text-align: center; font-size: 27px; line-height: 34px; padding-top: 2px; border-radius: 2px; }
  .back__footer { position: absolute; left: 18px; top: 718px; width: 520px; height: 46px; display: flex; align-items: center; }
  .back__footer .brand { font-size: 20px; }
  .badge { width: 44px; height: 44px; border-radius: 50%; background: #1f3f8f; border: 3px solid var(--white); margin-left: 22px; }
  .back__address { margin-left: auto; font-size: 16px; font-weight: 700; color: var(--white); }
</style>
</head>
<body>

<section class="panel panel--front">
  <div class="hero-photo" role="img" aria-label="Photo of a key with a house-shaped keyring in a door lock, brick wall behind"></div>
  <div class="front__lead">Want to</div>
  <div class="front__title">Enjoy</div>
  <div class="brand front__brand"><span class="brand__dot"></span>Brightkey Works</div>
  <div class="front__copy">
    <p class="front__peace">Peace of mind when not at home...</p>
    <p class="front__secure">Make sure your<br>Home is <em>SECURE</em> today!</p>
    <p class="front__turn">Turn over and fill out our quick check list,<br>If you think you need to improve security,<br>call us for a <em>FREE</em> quote</p>
  </div>
</section>

<section class="panel panel--back">
  <div class="back__intro">
    <p class="back__headline">There are a number of things you can do to reduce<br>the risk of having your home broken into.</p>
    <p class="back__advice">External door should be solid and fitted with high quality deadlocks.<br>Windows should also be fitted with secure locks. All locks should meet<br>Australian standards.</p>
    <p class="back__question">So how is your <em>security</em>?<br>Fill out our simple form and find out?</p>
  </div>

  <div class="checklist">
    <div class="checklist__head">
      <span class="checklist__head-left">Present Condition</span>
      <span class="checklist__head-right">Consider making changes<br>to items ticked NO</span>
    </div>

    <div class="checklist__body">
      <div class="group">
        <p class="group__title">Security Doors</p>
        <div class="item"><span>At all entry/exits</span><span class="item__yn">Y</span><span class="item__box"></span><span></span><span class="item__yn">N</span><span class="item__box"></span><span></span><span class="item__note">Security doors stop intruders from entering your home</span></div>
        <div class="item"><span>Finger Guards</span><span class="item__yn">Y</span><span class="item__box"></span><span></span><span class="item__yn">N</span><span class="item__box"></span><span></span><span class="item__note">Finger guards stop locks being tampered with</span></div>
        <div class="item"><span>Triple Locks</span><span class="item__yn">Y</span><span class="item__box"></span><span></span><span class="item__yn">N</span><span class="item__box"></span><span></span><span class="item__note">Provide extra strength for security doors</span></div>
      </div>
      <div class="group">
        <p class="group__title">Main Entry/Exit Doors</p>
        <div class="item"><span>Front - Solid core</span><span class="item__yn">Y</span><span class="item__box"></span><span></span><span class="item__yn">N</span><span class="item__box"></span><span></span><span class="item__note">Solid doors are preferred, as strong as locks</span></div>
        <div class="item"><span>Front - Viewer</span><span class="item__yn">Y</span><span class="item__box"></span><span></span><span class="item__yn">N</span><span class="item__box"></span><span></span><span class="item__note">Viewers help you see who is outside before opening</span></div>
        <div class="item"><span>Back - Solid core</span><span class="item__yn">Y</span><span class="item__box"></span><span></span><span class="item__yn">N</span><span class="item__box"></span><span></span><span class="item__note">Solid doors preferred, hollow doors should be avoided</span></div>
        <div class="item"><span>Adequate Locks</span><span class="item__yn">Y</span><span class="item__box"></span><span></span><span class="item__yn">N</span><span class="item__box"></span><span></span><span class="item__note">Deadlocks are the best type for entry/exit doors</span></div>
        <div class="item"><span>Keyed Alike</span><span class="item__yn">Y</span><span class="item__box"></span><span></span><span class="item__yn">N</span><span class="item__box"></span><span></span><span class="item__note">For ease of use and safety, one key opens all</span></div>
      </div>
      <div class="group">
        <p class="group__title">Sliding Doors</p>
        <div class="item"><span>Patio Locks</span><span class="item__yn">Y</span><span class="item__box"></span><span></span><span class="item__yn">N</span><span class="item__box"></span><span></span><span class="item__note">Keyed patio bolts on sliding doors strengthen security</span></div>
      </div>
      <div class="group">
        <p class="group__title">Windows</p>
        <div class="item"><span>Key Operated Locks</span><span class="item__yn">Y</span><span class="item__box"></span><span></span><span class="item__yn">N</span><span class="item__box"></span><span></span><span class="item__note">Key operated locks strengthen security</span></div>
        <div class="item"><span>Keyed Alike</span><span class="item__yn">Y</span><span class="item__box"></span><span></span><span class="item__yn">N</span><span class="item__box"></span><span></span><span class="item__note">For ease of use and safety, one key opens all</span></div>
        <div class="item"><span>Security Screens</span><span class="item__yn">Y</span><span class="item__box"></span><span></span><span class="item__yn">N</span><span class="item__box"></span><span></span><span class="item__note">Screens, grills and shutters add security and ventilation</span></div>
        <div class="item"><span>Warning Stickers</span><span class="item__yn">Y</span><span class="item__box"></span><span></span><span class="item__yn">N</span><span class="item__box"></span><span></span><span class="item__note">Warning stickers deter intruders</span></div>
      </div>
      <div class="group">
        <p class="group__title">Other</p>
        <div class="item"><span>Garage/Shed Secured</span><span class="item__yn">Y</span><span class="item__box"></span><span></span><span class="item__yn">N</span><span class="item__box"></span><span></span><span class="item__note">External buildings should be secured at all times</span></div>
        <div class="item"><span>Gates toYard Secured</span><span class="item__yn">Y</span><span class="item__box"></span><span></span><span class="item__yn">N</span><span class="item__box"></span><span></span><span class="item__note">Lock gates to yards with keyed padlock to stop intruders.</span></div>
      </div>
    </div>

    <div class="lock-photo" style="top:90px;height:44px" role="img" aria-label="Photo of a deadbolt and knob set"></div>
    <div class="lock-photo" style="top:142px;height:52px" role="img" aria-label="Photo of a rim deadlock"></div>
    <div class="lock-photo" style="top:200px;height:40px" role="img" aria-label="Photo of a door knob lock"></div>
    <div class="lock-photo" style="top:244px;height:40px" role="img" aria-label="Photo of a patio bolt lock"></div>
    <div class="lock-photo" style="top:292px;height:54px" role="img" aria-label="Photo of a digital keypad lock"></div>
    <div class="lock-photo" style="top:352px;height:30px" role="img" aria-label="Photo of a gate padlock"></div>

    <p class="checklist__cta">Need Assistance? Call us today for a FREE no obligation quote</p>
  </div>

  <div class="contact-bar">
    <p>P: 03 9000 4821 M: 0400 182 536</p>
    <p>www.brightkeyworks.com.au</p>
  </div>

  <div class="back__footer">
    <div class="brand"><span class="brand__dot"></span>Brightkey Works</div>
    <div class="badge" role="img" aria-label="Trade association badge"></div>
    <p class="back__address">PO Box 118 Fernvale Vic 3190</p>
  </div>
</section>

</body>
</html>
```